Glamorous package design for flat irons

I need a professionally designed box for my crystal flat irons. I would for the design for be glamorous. The irons are covered in rhinestones and very sparkly. I would like the package design to equally stand out. The name of these irons are Silk Wave Velvet Shine Presses.

I attached images of the current packaging, The flat irons and an idea of the colors I like. It doesn't have to be this color if you have better ideas.

I attached more images of box designs that I like. I love the bright colors. The box can be simple with the name of the irons on the front Silk Waves Shine Presses and the information I have posted below on the back the box doesn't have to include a picture of the irons or my logo

Target Market(s)

18 - 45

Font styles to use
Script

Requirements
Must have
• ( BLING ) I want the box design to catch the eye.
• The information I would like on the back on the box
• This beautiful pink ceramic flat Iron is decorated with sparkling rhinestones. Each stone was hand applied with a special heat-proof glue. Silk Waves Shine Presses provides fast extraordinary straightening results quick heat up and constant heat.
• Features:
• Ceramic plate, 1" width
• 1 hour automatic cut-off
• Ion technology to maximize silky and shiny results
• Professional 360 swivel cord to prevent tangling
• Digital LCD display shows the operating situation on the clear and active screen
• Temperature: 50°C~232°C/ 122°F~450°F
• Press temperature button '+' and '-' to turn into Fahrenheit.
Nice to have
• Diamonds, or sparkles I want the box to look expensive. Metallic silver
Should not have
• I do not want an open window on the box. I don't want any photos of the irons on the box. I want the design to make the statement.

```html
<!DOCTYPE html>
<html lang="en">
<head>
<meta charset="utf-8">
<title>Silk Wave Velvet Shine Presses – Box Front</title>
<link href="https://fonts.googleapis.com/css2?family=Montserrat:wght@800&family=Questrial&family=Playfair+Display:wght@400&display=swap" rel="stylesheet">
<style>
  :root {
    --stage: #ececec;
    --magenta-deep: #7e0f3c;
    --magenta: #a01a4f;
    --magenta-bright: #c8285f;
    --gold-light: #f6e2a6;
    --gold: #d4a84e;
    --gold-dark: #9c7224;
    --silver-light: #ffffff;
    --silver: #d9d9d9;
    --silver-dark: #9a9a9a;
    --brand-ink: #fbe9ef;
  }
  html, body {
    margin: 0;
    width: 1200px;
    height: 1000px;
    overflow: hidden;
    background: radial-gradient(ellipse at 40% 30%, #ffffff 0%, var(--stage) 70%);
  }
  .box-front {
    position: absolute;
    left: 80px;
    top: 335px;
    width: 1040px;
    height: 330px;
    overflow: hidden;
    background: linear-gradient(100deg, var(--magenta-deep) 0%, var(--magenta) 45%, var(--magenta-bright) 100%);
    box-shadow: 0 20px 40px rgba(0,0,0,0.18);
  }
  .bokeh {
    position: absolute;
    inset: 0;
    background:
      radial-gradient(circle at 8% 70%, rgba(255,180,210,0.22) 0, transparent 18%),
      radial-gradient(circle at 22% 30%, rgba(255,180,210,0.15) 0, transparent 14%),
      radial-gradient(circle at 78% 20%, rgba(255,180,210,0.15) 0, transparent 15%),
      radial-gradient(circle at 92% 75%, rgba(255,180,210,0.2) 0, transparent 16%);
  }
  .seal {
    position: absolute;
    left: 34px;
    top: 26px;
    width: 96px;
    height: 100px;
  }
  .brand {
    position: absolute;
    left: 0;
    right: 0;
    top: 40px;
    text-align: center;
    font-family: "Playfair Display", serif;
    font-size: 24px;
    color: var(--brand-ink);
    margin-left: 170px;
  }
  .brand-dot {
    display: inline-block;
    width: 10px;
    height: 10px;
    border-radius: 50%;
    background: var(--brand-ink);
    margin-left: 8px;
    vertical-align: middle;
  }
  .product-line {
    position: absolute;
    left: 0;
    right: 0;
    top: 86px;
    text-align: center;
    font-family: "Questrial", sans-serif;
    font-size: 42px;
    color: var(--gold);
    margin-left: -60px;
  }
  .product-name {
    position: absolute;
    left: 0;
    right: 0;
    top: 140px;
    text-align: center;
    font-family: "Montserrat", sans-serif;
    font-weight: 800;
    font-size: 100px;
    line-height: 1;
    letter-spacing: 1px;
    margin: 0;
  }
  .name-sparkle {
    background: linear-gradient(180deg, var(--silver-light) 0%, var(--silver) 50%, var(--silver-dark) 100%);
    -webkit-background-clip: text;
    background-clip: text;
    color: transparent;
  }
  .name-gold {
    background: linear-gradient(180deg, var(--gold-light) 0%, var(--gold) 55%, var(--gold-dark) 100%);
    -webkit-background-clip: text;
    background-clip: text;
    color: transparent;
  }
</style>
</head>
<body>
  <main class="box-front">
    <div class="bokeh" role="img" aria-label="Soft pink bokeh light background"></div>

    <svg class="seal" viewBox="0 0 96 100" aria-hidden="true">
      <defs>
        <radialGradient id="sealSilver" cx="40%" cy="35%" r="70%">
          <stop offset="0" stop-color="#ffffff"/>
          <stop offset="1" stop-color="#a8a8a8"/>
        </radialGradient>
        <linearGradient id="sealGold" x1="0" y1="0" x2="0" y2="1">
          <stop offset="0" stop-color="#f6e2a6"/>
          <stop offset="1" stop-color="#a87b2a"/>
        </linearGradient>
      </defs>
      <circle cx="48" cy="46" r="44" fill="url(#sealSilver)"/>
      <path d="M6 58 L90 58 L84 72 L90 86 L6 86 L12 72 Z" fill="url(#sealGold)"/>
    </svg>

    <div class="brand">Silk Crest Inc.<span class="brand-dot"></span></div>
    <div class="product-line">Silk Wave Velvet</div>
    <h1 class="product-name"><span class="name-sparkle">SHINE</span> <span class="name-gold">PRESSES</span></h1>
  </main>
</body>
</html>
```